Modern Business Card for Industrial Company

We need business cards updated with modern fonts and make it look more technical, sharp and clean. The logo should not be changed, but we are looking for fresh solutions for how other information on the card is laid out in an interesting way. The company provides machinery and services to the ceramic industry and deals with cutting-edge technology. The design should reflect a technologically advanced and modern company that deals with the latest European technologies.

Font styles to use
Sans Serif

Requirements
Must have
• Modern fonts, technical look and feel

```html
<!DOCTYPE html>
<html lang="en">
<head>
<meta charset="utf-8">
<title>Kerant Systems – Business Card</title>
<link rel="stylesheet" href="https://fonts.googleapis.com/css2?family=Bebas+Neue&family=Open+Sans:wght@400;600&display=swap">
<style>
  :root {
    --brand-blue: #06548f;
    --brand-blue-light: #0b68ae;
    --brand-red: #b22228;
    --text-grey: #474747;
    --backdrop: #c4c4c4;
    --card-white: #ffffff;
  }
  * { margin: 0; padding: 0; box-sizing: border-box; }
  html, body {
    width: 1093px; height: 1200px; overflow: hidden;
    background: var(--backdrop);
    font-family: "Open Sans", sans-serif;
  }
  .card {
    position: absolute; left: 264px; width: 580px; height: 357px;
  }
  .card-front { top: 226px; background: var(--card-white); }
  .card-back { top: 620px; background: var(--brand-blue); }

  .brand {
    position: absolute; left: 27px; top: 58px;
    display: flex; align-items: center; gap: 12px;
  }
  .brand-square { width: 30px; height: 30px; background: var(--brand-blue); }
  .brand-name {
    font-weight: 600; font-size: 34px; color: var(--brand-blue);
    letter-spacing: 0.5px; line-height: 1;
  }

  .address {
    position: absolute; left: 28px; top: 198px;
    font-size: 15.5px; line-height: 21px; color: var(--text-grey);
  }
  .contacts {
    position: absolute; left: 33px; top: 254px; list-style: none;
    font-size: 15.5px; line-height: 21px; color: var(--text-grey);
  }
  .contacts li { display: flex; align-items: center; gap: 6px; }
  .contacts svg { width: 15px; height: 15px; flex: none; }
  .contacts .accent { color: var(--brand-blue); }

  .person {
    position: absolute; right: 36px; top: 226px; text-align: right;
  }
  .person-name {
    font-family: "Bebas Neue", sans-serif; font-size: 33px; line-height: 1;
    color: var(--brand-blue); letter-spacing: 0.2px;
  }
  .person-title { font-size: 15px; color: var(--text-grey); margin-top: 2px; }

  .card-stripe { position: absolute; left: 0; bottom: 0; width: 580px; height: 14px; display: block; }

  .back-brand {
    position: absolute; inset: 0;
    display: flex; align-items: center; justify-content: center;
    font-weight: 600; font-size: 58px; color: var(--brand-blue-light);
    letter-spacing: 1px;
  }
</style>
</head>
<body>
  <section class="card card-front">
    <div class="brand">
      <span class="brand-square"></span>
      <span class="brand-name">Kerant Systems</span>
    </div>

    <address class="address" style="font-style:normal">
      418 Vega Parkway, Suite 200<br>
      Norcliff, GA 30120
    </address>

    <ul class="contacts">
      <li>
        <svg viewBox="0 0 16 16" aria-hidden="true"><path fill="var(--brand-blue)" d="M3.6 1.2l2.3 2.6-1.3 1.8c.9 2 2.5 3.6 4.5 4.6l1.8-1.3 2.6 2.3-1.4 2.2C6.8 13.3 2.7 9.2 1.2 3.9z"/><path d="M9.5 2.5a4.5 4.5 0 0 1 4 4M9.2 4.7a2.3 2.3 0 0 1 2.1 2.1" stroke="var(--brand-blue)" stroke-width="1.3" fill="none"/></svg>
        <span>21 555-0184</span>
      </li>
      <li>
        <svg viewBox="0 0 16 16" aria-hidden="true"><rect x="0.5" y="3" width="15" height="10" fill="var(--brand-blue)"/><path d="M1 3.5l7 5.5 7-5.5M1 12.5l5-4.5M15 12.5l-5-4.5" stroke="#fff" stroke-width="1.1" fill="none"/></svg>
        <span>mbellandi@kerantsys.com</span>
      </li>
      <li>
        <svg viewBox="0 0 16 16" aria-hidden="true"><g stroke="var(--brand-blue)" stroke-width="1.2" fill="none"><circle cx="8" cy="8" r="6.8"/><ellipse cx="8" cy="8" rx="3" ry="6.8"/><path d="M1.2 8h13.6M2.3 4.5h11.4M2.3 11.5h11.4M8 1.2v13.6"/></g></svg>
        <span>www.<span class="accent">kerantsys</span>.com</span>
      </li>
    </ul>

    <div class="person">
      <div class="person-name">Marco Bellandi</div>
      <div class="person-title">President</div>
    </div>

    <svg class="card-stripe" viewBox="0 0 580 14" preserveAspectRatio="none" aria-hidden="true">
      <polygon points="0,0 294,0 300,14 0,14" fill="var(--brand-blue)"/>
      <polygon points="300,0 580,0 580,14 306,14" fill="var(--brand-red)"/>
    </svg>
  </section>

  <section class="card card-back">
    <div class="back-brand">Kerant Systems</div>
  </section>
</body>
</html>
```